Drone company needs a brochure design

We would like a brochure design which compliments our existing logo, website and business card designs.

www.bramblecrest.com.au

```html
<!DOCTYPE html>
<html lang="en">
<head>
<meta charset="utf-8">
<title>Bramble Crest – Brochure</title>
<link rel="stylesheet" href="https://fonts.googleapis.com/css2?family=Montserrat:wght@400;600;700&display=swap">
<style>
  :root {
    --blue: #29a9e1;
    --black: #000000;
    --white: #ffffff;
    --ink: #2a2a2a;
    --fold: #e6478d;
    --page: #ffffff;
    --frame: #3a3a3a;
  }
  * { box-sizing: border-box; margin: 0; padding: 0; }
  html, body { width: 1200px; height: 612px; overflow: hidden; background: var(--page); }
  body { position: relative; font-family: "Montserrat", Arial, sans-serif; color: var(--ink); }

  .sheet { position: absolute; top: 50px; width: 531px; height: 376px; overflow: hidden; border: 1px solid var(--frame); }
  .sheet--outside { left: 51px; }
  .sheet--inside { left: 618px; background: var(--white); }

  .photo { position: absolute; }
  .fold { position: absolute; top: 0; bottom: 0; width: 0; border-left: 1px dashed var(--fold); }

  /* outside */
  .about-panel { position: absolute; left: 0; top: 0; width: 177px; height: 206px; background: var(--black); color: var(--white); }
  .about-title { position: absolute; left: 27px; top: 26px; font-size: 19px; font-weight: 700; color: var(--blue); letter-spacing: 0.2px; display: flex; align-items: center; gap: 3px; }
  .about-copy { position: absolute; left: 27px; top: 54px; width: 130px; font-size: 5.5px; line-height: 8.8px; }
  .about-copy p + p { margin-top: 8px; }
  .services-title { position: absolute; left: 27px; top: 188px; font-size: 19px; font-weight: 700; color: var(--white); line-height: 1; }
  .photo--harbour { left: 0; top: 206px; width: 177px; height: 170px; background: linear-gradient(180deg, #9fbfe0 0%, #c9d6e2 30%, #7b8a96 42%, #2d5a8c 50%, #1d4778 100%); }
  .photo--city { left: 177px; top: 0; width: 354px; height: 376px; background: linear-gradient(180deg, #7aa6de 0%, #a8c3e6 24%, #6f7a7c 38%, #5c6e58 58%, #4f7a46 78%, #3f7c3a 100%); }
  .photo--city::after { content: ""; position: absolute; right: 0; top: 190px; width: 110px; height: 186px; background: linear-gradient(180deg, #3f6fa8, #2e5f98); }

  .brand-box { position: absolute; left: 355px; top: 31px; width: 176px; height: 59px; background: var(--white); display: flex; align-items: center; justify-content: center; gap: 6px; }
  .brand-name { font-size: 15px; font-weight: 700; color: var(--black); }
  .brand-mark { width: 9px; height: 9px; border-radius: 50%; background: var(--blue); }

  .contact-box { position: absolute; left: 179px; top: 287px; width: 175px; height: 59px; background: var(--white); text-align: center; font-size: 5.6px; line-height: 8px; color: var(--ink); }
  .contact-icons { display: flex; justify-content: center; gap: 6px; margin: 9px 0 4px; }
  .contact-icon { width: 14px; height: 14px; border-radius: 2px; background: var(--blue); display: flex; align-items: center; justify-content: center; }

  /* inside */
  .photo--estate { left: 0; top: 0; width: 531px; height: 144px; background: linear-gradient(180deg, #6fa4de 0%, #b7cfe8 22%, #4d7a3a 34%, #3e6a2e 58%, #1f5fae 66%, #2a66b2 100%); }
  .services { position: absolute; left: 0; top: 144px; width: 531px; height: 232px; }
  .service { position: absolute; width: 134px; font-size: 5.5px; line-height: 8px; color: var(--ink); overflow-wrap: break-word; }
  .service-icon { width: 29px; height: 29px; border-radius: 50%; background: var(--blue); opacity: 0.85; display: flex; align-items: center; justify-content: center; margin-bottom: 5px; }
  .service-title { color: var(--blue); font-weight: 600; font-size: 5.8px; }

  .band { position: absolute; left: 0; top: 478px; width: 1200px; height: 134px; background: var(--black); }
  .band-brand { position: absolute; right: 51px; top: 40px; display: flex; align-items: center; gap: 8px; }
  .band-brand .brand-name { color: var(--white); font-size: 22px; }
</style>
</head>
<body>

  <section class="sheet sheet--outside">
    <div class="photo photo--city" role="img" aria-label="Aerial view of a city skyline beside a river foreshore and parkland"></div>

    <div class="about-panel">
      <h2 class="about-title">about
        <svg width="9" height="9" viewBox="0 0 10 10" aria-hidden="true"><path d="M1 1l4 3 4-3M1 5l4 3 4-3" fill="none" stroke="#29a9e1" stroke-width="1.6"/></svg>
      </h2>
      <div class="about-copy">
        <p>We provide premium aerial media solutions using the latest Unmanned Aerial Vehicles (UAV) technology. Offering a combination of stunning HD aerial filming and breathtaking aerial photography for a variety of different projects. The Bramble Crest team offer a unique service that is bespoke to your application and desired specification.</p>
        <p>Let us capture your vision and provide you with that ultimate vantage!</p>
      </div>
    </div>
    <h2 class="services-title">«services</h2>
    <div class="photo photo--harbour" role="img" aria-label="Harbour with a small boat on the water in front of port buildings"></div>

    <div class="fold" style="left:177px"></div>
    <div class="fold" style="left:355px"></div>

    <div class="brand-box">
      <span class="brand-mark"></span>
      <span class="brand-name">Bramble Crest</span>
    </div>

    <div class="contact-box">
      <div class="contact-icons">
        <span class="contact-icon"><svg width="8" height="8" viewBox="0 0 10 10" aria-hidden="true"><path d="M2 1l2 2-1 1.2c.6 1.3 1.5 2.2 2.8 2.8L7 6l2 2-1.3 1.3C4.5 9 1 5.5.7 2.3z" fill="#fff"/></svg></span>
        <span class="contact-icon"><svg width="9" height="7" viewBox="0 0 10 8" aria-hidden="true"><rect x=".5" y=".5" width="9" height="7" fill="none" stroke="#fff"/><path d="M.5.5l4.5 4 4.5-4" fill="none" stroke="#fff"/></svg></span>
      </div>
      <div>0400 555 018</div>
      <div>contact@bramblecrest.com.au</div>
      <div>COVEDALE, WA 6999</div>
    </div>
  </section>

  <section class="sheet sheet--inside">
    <div class="photo photo--estate" role="img" aria-label="Aerial view of a lakeside estate with a fountain, trees and vineyards"></div>
    <div class="services">
      <div class="fold" style="left:176px; top:2px"></div>
      <div class="fold" style="left:353px; top:2px"></div>

      <article class="service" style="left:29px; top:12px">
        <div class="service-icon"><svg width="16" height="12" viewBox="0 0 16 12" aria-hidden="true"><path d="M1 6l7-5 7 5M3 5v6h10V5" fill="none" stroke="#fff" stroke-width="1.3"/></svg></div>
        <div class="service-title">Real Estate</div>
        <p>Buyers want to learn about the area surrounding their property as much as they want to learn about the property itself.<br>Bramble Crest can showcase important factors like proximity to the coast, lakes, schools, major transport, CBD and the general feel of an area.</p>
      </article>
      <article class="service" style="left:206px; top:12px">
        <div class="service-icon"><svg width="16" height="14" viewBox="0 0 16 14" aria-hidden="true"><path d="M1 4l4-2 6 2 4-2v8l-4 2-6-2-4 2z" fill="none" stroke="#fff" stroke-width="1.2"/></svg></div>
        <div class="service-title">Survey &amp; Mapping</div>
        <p>Reliable, timely survey data to enhance productivity or for precise Geo-location.<br>Cost-effective alternative to conventional aerial surveys &amp; mapping.<br>We are mobile and can travel to remote mine sights and rural farming operations.</p>
      </article>
      <article class="service" style="left:383px; top:12px">
        <div class="service-icon"><svg width="16" height="14" viewBox="0 0 16 14" aria-hidden="true"><rect x="1" y="1" width="14" height="9" fill="none" stroke="#fff" stroke-width="1.3"/><path d="M6 13h4M8 10v3" stroke="#fff" stroke-width="1.3"/></svg></div>
        <div class="service-title">Media &amp; Advertising</div>
        <p>Aerial video and photography are ideal for websites and almost all promotional publications where you need a new perspective to show your products or services to new clients.<br>Let us help you stand out from the pack.</p>
      </article>

      <article class="service" style="left:29px; top:112px">
        <div class="service-icon"><svg width="10" height="16" viewBox="0 0 10 16" aria-hidden="true"><rect x="1" y="1" width="8" height="14" fill="none" stroke="#fff" stroke-width="1.3"/><path d="M3 4h4M3 7h4M3 10h4" stroke="#fff"/></svg></div>
        <div class="service-title">Construction &amp; Property</div>
        <p>We can help you affordably track the progression of your developments so you can update your clients with stunning aerial photos and HD video.<br>Also providing existing properties such as Golf Courses, Hotel Resorts aerial imagery that showcases their properties.</p>
      </article>
      <article class="service" style="left:206px; top:112px">
        <div class="service-icon"><svg width="16" height="15" viewBox="0 0 16 15" aria-hidden="true"><path d="M4 9a3 3 0 010-6 4 4 0 017 0 3 3 0 011 6z" fill="#fff"/><path d="M5 11l-1 3M8 11l-1 3M11 11l-1 3" stroke="#fff"/></svg></div>
        <div class="service-title">Insurance &amp; Risk</div>
        <p>Bramble Crest are pleased to work with local insurance companies to inspect damage caused to land and properties.<br>Assisting assessors and loss adjustors for claims.<br>We also provide risk surveying support for underwriters.</p>
      </article>
      <article class="service" style="left:383px; top:112px">
        <div class="service-icon"><svg width="15" height="15" viewBox="0 0 15 15" aria-hidden="true"><circle cx="9" cy="6" r="4.5" fill="none" stroke="#fff" stroke-width="1.4"/><path d="M5.8 9.2L1.5 13.5" stroke="#fff" stroke-width="1.8"/></svg></div>
        <div class="service-title">Inspection &amp; Environment</div>
        <p>We eliminate the need for expensive and time consuming scaffolding, man-lifting equipment and helicopter charters.<br>Our cameras can be viewed in real-time from the ground by your qualified technicians and we can take in-flight instructions in order to provide the perfect vantage for their specific needs.</p>
      </article>
    </div>
  </section>

  <footer class="band">
    <div class="band-brand">
      <span class="brand-mark"></span>
      <span class="brand-name">Bramble Crest</span>
    </div>
  </footer>

</body>
</html>
```